Double caffeinated coffee label design

We need to design labels for a new coffee brand. The label size: 2.75” x 4.125” (Corners slightly rounded). There will be front and back label in stickers to be put on standardized bags. Our product is roasted whole bean and ground coffee in 12oz bags. It is described as "strong, bold, intense, and double caffeinated. The product is designed for passionate coffee drinkers who want strong, more caffeinated but not bitter coffee. The coffee is suitable for espresso base coffees.
Target Market(s)
Groceries, food stores, super markets. Heavy and sophisticated coffee drinkers.
Requirements
Must have
- Modern, minimalist style. Strong and bold look. Creative. Impressive.
Nice to have
- Some impressed coffee label designs for reference: https://www.trevalo.net/find?q=most+impressive+coffee+brand+designs&from=qwer&kind=pics&sa=Y&ref=7bZkQxmPtLrsWvNcYhDjKeFgAoUiBnMwZpRsTeQvLbXy_KHJaPqWz&vw=1280&vh=610#pic=kR4mTzWqPxNbLo:

```html
<!DOCTYPE html>
<html lang="en">
<head>
<meta charset="utf-8">
<title>Boldmark Coffee – Roasted Whole Bean Label</title>
<link rel="stylesheet" href="https://fonts.googleapis.com/css2?family=Open+Sans:wght@400;600&family=Kaushan+Script&family=Libre+Baskerville&display=swap">
<style>
  :root {
    --page-bg: #ffffff;
    --label-black: #231f20;
    --accent-orange: #ee5a2b;
    --text-white: #ffffff;
  }
  html, body {
    margin: 0;
    padding: 0;
    width: 1200px;
    height: 1085px;
    overflow: hidden;
    background: var(--page-bg);
  }
  .canvas {
    position: relative;
    width: 1200px;
    height: 1085px;
  }
  .label {
    position: absolute;
    left: 300px;
    top: 92px;
    width: 600px;
    height: 902px;
    background: var(--label-black);
    border-radius: 34px;
    overflow: hidden;
    color: var(--text-white);
  }
  .brand {
    position: absolute;
    left: 0;
    right: 0;
    top: 300px;
    text-align: center;
    font-family: "Open Sans", sans-serif;
    font-weight: 600;
    color: var(--text-white);
  }
  .brand-row {
    display: inline-flex;
    align-items: center;
    gap: 14px;
  }
  .brand-dot {
    width: 18px;
    height: 18px;
    border-radius: 50%;
    background: var(--accent-orange);
  }
  .brand-name {
    font-size: 62px;
    line-height: 1;
    letter-spacing: 1px;
  }
  .brand-sub {
    display: block;
    margin-top: 10px;
    font-size: 18px;
    letter-spacing: 5px;
  }
  .rule {
    position: absolute;
    left: 0;
    right: 0;
    height: 2px;
    background: var(--accent-orange);
  }
  .rule-top { top: 506px; }
  .rule-bottom { top: 606px; }
  .product-band {
    position: absolute;
    left: 0;
    right: 0;
    top: 514px;
    height: 86px;
    background: var(--accent-orange);
    display: flex;
    align-items: center;
    justify-content: center;
  }
  .product-name {
    font-family: "Kaushan Script", cursive;
    font-size: 52px;
    color: var(--text-white);
    line-height: 1;
  }
  .tagline {
    position: absolute;
    left: 0;
    right: 0;
    top: 620px;
    text-align: center;
    font-family: "Open Sans", sans-serif;
    font-size: 18px;
    letter-spacing: 1.4px;
    color: var(--accent-orange);
    word-spacing: 2px;
  }
  .tagline .sep { margin: 0 10px; }
  .usage {
    position: absolute;
    left: 0;
    right: 0;
    top: 702px;
    text-align: center;
    font-family: "Libre Baskerville", serif;
  }
  .usage-title {
    display: block;
    font-size: 17px;
    letter-spacing: 2px;
  }
  .usage-detail {
    display: block;
    margin-top: 8px;
    font-size: 13px;
    letter-spacing: 1.6px;
  }
  .origin, .net-weight {
    position: absolute;
    top: 808px;
    font-family: "Libre Baskerville", serif;
    font-size: 14px;
    line-height: 1.4;
  }
  .origin { left: 50px; }
  .net-weight { right: 50px; text-align: right; }
</style>
</head>
<body>
<div class="canvas">
  <section class="label">
    <div class="brand">
      <span class="brand-row">
        <span class="brand-dot"></span>
        <span class="brand-name">Boldmark</span>
      </span>
      <span class="brand-sub">COFFEE</span>
    </div>

    <div class="rule rule-top"></div>
    <div class="product-band">
      <span class="product-name">Roasted Whole Bean</span>
    </div>
    <div class="rule rule-bottom"></div>

    <p class="tagline">STRONG<span class="sep">•</span>BOLD<span class="sep">•</span>INTENSE<span class="sep">•</span>DOUBLE CAFFEINATED</p>

    <div class="usage">
      <span class="usage-title">SUITABLE FOR</span>
      <span class="usage-detail">ESPRESSO BASE COFFEES</span>
    </div>

    <div class="origin">Roasted in USA</div>
    <div class="net-weight">Net Wt / Poids Net<br>12oz (300g)</div>
  </section>
</div>
</body>
</html>
```